bluegum ridge coaching needs snazzy business card that serves a dual purpose

business card needed for a Bluegum Ridge Coaching company that takes people out on the road to teach them proficiency on their bike.
My business logo is attached. I have grey and aqua colours with my logo.
i really like bitumen/tarmac/ road in the design somehow but that is up to you.
I think navy blue will go well with my colours too. see how you go.

I want this card to look REALLY good.
the back of the card may be used for emergency contact details too
In case of Emergency I am:
Name:

Emergency Contact name
emergency contact Phone number:

• details that are essential are:
• logo
• Name: Helena FORD
• ABN: 53 291 804 667
• phone number: 0455 128 906
• chatterly logo
• * ride tuition & proficiency
• * skills practice
• * maintenance 101
• * bike fitting service
• * cater for all ages & abilities
• backpage:
• logo
• skills confidence enjoyment
• some space for writing
• nothing girly. The business will already naturally attract women, it needs to appeal to both genders

```html
<!DOCTYPE html>
<html lang="en">
<head>
<meta charset="utf-8">
<title>Bluegum Ridge Coaching – Business Card</title>
<link href="https://fonts.googleapis.com/css2?family=Open+Sans:ital,wght@0,400;0,600;0,700;1,700&display=swap" rel="stylesheet">
<style>
  :root {
    --page: #e9e7e3;
    --card: #3a3a3c;
    --card-shadow: rgba(0, 0, 0, 0.28);
    --ink: #ffffff;
    --ink-soft: #e6e6e6;
    --aqua: #5cc6b4;
    --band-grey: #5c5c5f;
    --faint: #474749;
  }
  * { box-sizing: border-box; margin: 0; padding: 0; }
  html, body {
    width: 1200px;
    height: 900px;
    overflow: hidden;
    background: var(--page);
    font-family: "Open Sans", Arial, sans-serif;
  }
  .sheet {
    position: relative;
    width: 1200px;
    height: 900px;
  }
  .card {
    position: absolute;
    left: 280px;
    width: 640px;
    height: 366px;
    background: var(--card);
    border-radius: 4px;
    overflow: hidden;
    box-shadow: 0 14px 30px var(--card-shadow);
  }
  .card--back { top: 52px; }
  .card--front { top: 482px; }

  /* Back */
  .back-mark {
    position: absolute;
    left: 150px;
    top: 38px;
    width: 290px;
    height: 290px;
    border-radius: 50%;
    background: var(--faint);
  }
  .back-tagline {
    position: absolute;
    left: 205px;
    top: 210px;
    color: var(--ink);
    font-size: 15px;
    font-weight: 700;
    font-style: italic;
    letter-spacing: 0.2px;
  }

  /* Front */
  .brand {
    position: absolute;
    left: 0;
    right: 0;
    top: 74px;
    display: flex;
    align-items: center;
    justify-content: center;
    gap: 14px;
  }
  .brand-dot {
    width: 30px;
    height: 30px;
    border-radius: 50%;
    background: var(--aqua);
  }
  .brand-name {
    color: var(--aqua);
    font-size: 34px;
    font-weight: 600;
    letter-spacing: 0.5px;
  }
  .brand-rule {
    position: absolute;
    left: 120px;
    top: 136px;
    width: 200px;
    height: 2px;
    background: var(--ink);
  }
  .holder {
    position: absolute;
    left: 0;
    right: 0;
    top: 154px;
    text-align: center;
    color: var(--ink);
  }
  .holder-name {
    font-size: 24px;
    font-weight: 700;
    letter-spacing: 0.3px;
  }
  .holder-contact {
    margin-top: 6px;
    font-size: 13px;
    color: var(--ink-soft);
  }
  .services {
    margin-top: 12px;
    font-size: 16px;
    line-height: 1.45;
    color: var(--ink);
  }
  .social {
    position: absolute;
    right: 26px;
    top: 150px;
    display: flex;
    align-items: center;
    gap: 6px;
    color: var(--ink);
    font-size: 12px;
    font-weight: 400;
  }
  .social-square {
    width: 18px;
    height: 18px;
    background: var(--ink);
  }
  .bands {
    position: absolute;
    left: 0;
    bottom: 0;
    width: 640px;
    height: 60px;
  }
</style>
</head>
<body>
  <main class="sheet">
    <section class="card card--back" aria-label="Card back">
      <div class="back-mark" aria-hidden="true"></div>
      <p class="back-tagline">skills confidence enjoyment</p>
    </section>

    <section class="card card--front" aria-label="Card front">
      <div class="brand">
        <span class="brand-dot" aria-hidden="true"></span>
        <span class="brand-name">Bluegum Ridge Coaching</span>
      </div>
      <div class="brand-rule" aria-hidden="true"></div>

      <div class="social">
        <span class="social-square" aria-hidden="true"></span>
        <span>chatterly</span>
      </div>

      <div class="holder">
        <p class="holder-name">Helena FORD</p>
        <p class="holder-contact">0455 128 906 | ABN: 53 291 804 667</p>
        <div class="services">
          <p>Ride tuition &amp; proficiency • Skills practice • Maintenance 101</p>
          <p>Bike fitting service • Cater for all ages &amp; abilities</p>
        </div>
      </div>

      <svg class="bands" viewBox="0 0 640 60" aria-hidden="true">
        <polygon points="0,30 360,30 380,60 0,60" fill="var(--band-grey)"/>
        <polygon points="300,32 640,18 640,60 330,60" fill="var(--aqua)"/>
      </svg>
    </section>
  </main>
</body>
</html>
```